Hi Designers,

I will need 4 web pages designed. The web page looks like an App (if you click on the logo, or the icon on an iPad, it will take you to the website), but it is still a webpage.

Please check the attachment on this brief to understand what specific pages I need to be designed.

A .PSD (straight-up PhotoShop image) as final deliverable is fine, as long as you give us the exact “web color numbers”.

The design is for desktop and iPad but in a single unified web application, NOT separate web app and (native) iPad app.

Details:

Bright Harbor Policy Systems is developing a browser-based application for use on any mobile device or desktop. The app will be used by corporations to communicate with their employees regarding legal, regulatory and company requirements for conducting business. The app is known as “Workplace Guidance Hub.” When the user clicks on the icon for Workplace Guidance Hub, they will enter a site full of information that a company deems necessary for the employee to do his/her job. There are several content sections within the site, including a login page, training, policies, forms, news feeds and blogs.

The application has been built using Microsoft .NET, and fully supports CSS-type skinning; it uses traditional page layouts. We are seeking a product logo concept (image), a master application/desktop icon (image), as well as a full color scheme/theme/skin design for all areas of the application (header area, body text, menu bar, etc.) in the form of a CSS. The look should be clean, crisp and professional; nothing cartoony or whimsical. It should be easy to read and “airy”.

We have sketched prototypes for the basic application page layout that we can send as a next step of the process.
Updates

Screen shots have been uploaded to this project.  Please use them to guide your design.

Dear designers,

I apologize for the delay in providing feedback. My partners and I will provide feedback in a few days. Thank you for your patience.

Industry/Entity Type

Business

Font styles to use
Other font styles liked:
• see font on screen shots when uploaded

```html
<!DOCTYPE html>
<html lang="en">
<head>
<meta charset="utf-8">
<title>Workplace Guidance Hub – Sign In and Home</title>
<link href="https://fonts.googleapis.com/css2?family=Open+Sans:wght@400;600;700&display=swap" rel="stylesheet">
<style>
:root{
  --navy:#0b2a50;
  --navy-btn:#0d2f57;
  --status:#141414;
  --page:#ffffff;
  --body-light:#f3f3f3;
  --body-mid:#e6e6e6;
  --text:#2a2a2a;
  --link:#1f4a86;
  --tile-top:#fbfbfb;
  --tile-bottom:#ececec;
  --tile-border:#d4d4d4;
  --icon:#2d2d2d;
}
*{box-sizing:border-box;margin:0;padding:0}
html,body{width:1200px;height:1094px;overflow:hidden;background:var(--page)}
body{position:relative;font-family:"Open Sans",Arial,sans-serif;color:var(--text)}
.screen{position:absolute;top:255px;width:394px;height:595px;overflow:hidden;background:var(--body-mid)}
.screen--signin{left:137px;background:radial-gradient(ellipse at 60% 40%,#fdfdfd 0%,var(--body-light) 45%,#ececec 100%)}
.screen--home{left:675px;background:linear-gradient(#e2e2e2,#e8e8e8)}
.status-bar{height:26px;background:var(--status);color:#fff;font:700 15px/26px Arial,Helvetica,sans-serif;position:relative;padding-left:6px;display:flex;align-items:center;gap:4px}
.status-bar .carrier{margin-left:2px}
.status-bar .net{margin-left:8px}
.status-bar .lock{position:absolute;left:190px;top:6px}
.status-bar .battery{position:absolute;right:4px;top:8px}
.app-header{height:52px;background:var(--navy);color:#fff;position:relative}
.brand-name{position:absolute;left:74px;top:0;line-height:58px;font-size:14px;font-weight:400}
.hub-title{position:absolute;right:13px;top:0;line-height:58px;font-size:13.5px;font-weight:700}
.signin-form{position:absolute;left:29px;top:197px;width:336px}
.field-label{display:block;font-size:14.5px;margin-bottom:8px}
.field-input{display:block;width:336px;height:41px;border:1px solid #dcdcdc;border-radius:2px;background:linear-gradient(#ffffff,#f0f0f0);margin-bottom:21px}
.form-links{font-size:14.5px;margin-top:2px}
.form-links .sep{margin:0 8px}
.form-links a{color:var(--link);text-decoration:none}
.btn-signin{position:absolute;left:1px;top:199px;width:94px;height:38px;background:var(--navy-btn);color:#fff;border-radius:2px;font-size:14.5px;display:flex;align-items:center;justify-content:center;gap:7px}
.btn-home{position:absolute;left:23px;top:14px;height:27px;padding:0 8px 0 18px;background:linear-gradient(#ffffff,#dcdcdc);color:#222;font-size:13.5px;line-height:27px;clip-path:polygon(12px 0,100% 0,100% 100%,12px 100%,0 50%)}
.user-menu{position:absolute;right:22px;top:0;line-height:55px;font-size:14px;font-weight:700}
.tile{position:absolute;width:167px;height:83px;background:linear-gradient(var(--tile-top),var(--tile-bottom));border:1px solid var(--tile-border);box-shadow:0 1px 2px rgba(0,0,0,.12);display:flex;align-items:center;padding-left:16px;gap:12px;font-size:14.5px;line-height:20px}
.tile svg{flex:none}
</style>
</head>
<body>

<section class="screen screen--signin">
  <div class="status-bar">
    <svg width="22" height="12" viewBox="0 0 22 12" fill="#fff"><rect x="0" y="9" width="3" height="3"/><rect x="4" y="7" width="3" height="5"/><rect x="8" y="5" width="3" height="7"/><rect x="12" y="3" width="3" height="9"/><rect x="16" y="0" width="3" height="12"/></svg>
    <span class="carrier">NOVA</span><span class="net">3G</span>
    <svg class="lock" width="12" height="15" viewBox="0 0 12 15"><path d="M3 7V4.5a3 3 0 0 1 6 0V7" stroke="#ddd" stroke-width="2" fill="none"/><rect x="1" y="7" width="10" height="8" fill="#ddd"/></svg>
    <svg class="battery" width="26" height="11" viewBox="0 0 26 11"><rect x=".5" y=".5" width="22" height="10" fill="none" stroke="#fff"/><rect x="2" y="2" width="19" height="7" fill="#fff"/><rect x="23" y="3" width="2" height="5" fill="#fff"/></svg>
  </div>
  <header class="app-header">
    <span class="brand-name">Veltrana</span>
    <span class="hub-title">Workplace Guidance Hub</span>
  </header>
  <form class="signin-form">
    <label class="field-label">Username</label>
    <span class="field-input"></span>
    <label class="field-label">Password</label>
    <span class="field-input"></span>
    <p class="form-links">Keep me signed in<span class="sep">|</span><a href="#">Forgot Password?</a></p>
    <span class="btn-signin">
      <svg width="11" height="14" viewBox="0 0 11 14"><path d="M2.5 6.5V4a3 3 0 0 1 6 0v2.5" stroke="#fff" stroke-width="1.8" fill="none"/><rect x="0" y="6.5" width="11" height="7.5" fill="#fff"/></svg>
      Sign In
    </span>
  </form>
</section>

<section class="screen screen--home">
  <div class="status-bar">
    <svg width="22" height="12" viewBox="0 0 22 12" fill="#fff"><rect x="0" y="9" width="3" height="3"/><rect x="4" y="7" width="3" height="5"/><rect x="8" y="5" width="3" height="7"/><rect x="12" y="3" width="3" height="9"/><rect x="16" y="0" width="3" height="12"/></svg>
    <span class="carrier">NOVA</span><span class="net">3G</span>
    <svg class="lock" width="12" height="15" viewBox="0 0 12 15"><path d="M3 7V4.5a3 3 0 0 1 6 0V7" stroke="#ddd" stroke-width="2" fill="none"/><rect x="1" y="7" width="10" height="8" fill="#ddd"/></svg>
    <svg class="battery" width="26" height="11" viewBox="0 0 26 11"><rect x=".5" y=".5" width="22" height="10" fill="none" stroke="#fff"/><rect x="2" y="2" width="19" height="7" fill="#fff"/><rect x="23" y="3" width="2" height="5" fill="#fff"/></svg>
  </div>
  <header class="app-header">
    <span class="btn-home">Home</span>
    <span class="user-menu">Marcus ▾</span>
  </header>

  <div class="tile" style="left:24px;top:154px">
    <svg width="44" height="36" viewBox="0 0 44 36" fill="none" stroke="var(--icon)" stroke-width="3"><rect x="2" y="2" width="40" height="32"/><line x1="2" y1="9" x2="42" y2="9"/><rect x="8" y="14" width="12" height="14" fill="var(--icon)"/><line x1="24" y1="15" x2="37" y2="15"/><line x1="24" y1="21" x2="37" y2="21"/><line x1="24" y1="27" x2="37" y2="27"/></svg>
    <span>Compliance<br>News</span>
  </div>
  <div class="tile" style="left:204px;top:154px">
    <svg width="42" height="40" viewBox="0 0 42 40" fill="none" stroke="var(--icon)" stroke-width="4" stroke-linecap="round"><path d="M6 6v20a8 8 0 1 0 8-8"/><path d="M20 12a14 14 0 0 1 12 14"/><path d="M22 3a22 22 0 0 1 17 23"/></svg>
    <span>Compliance<br>Blog</span>
  </div>
  <div class="tile" style="left:24px;top:248px">
    <svg width="42" height="42" viewBox="0 0 42 42"><circle cx="21" cy="21" r="20" fill="var(--icon)"/><path d="M14.5 16a6.5 6.5 0 1 1 9 6c-2 1-2.5 2-2.5 4" stroke="#fff" stroke-width="4.5" fill="none"/><circle cx="21" cy="32" r="2.8" fill="#fff"/></svg>
    <span>FAQ’s</span>
  </div>
  <div class="tile" style="left:204px;top:248px">
    <svg width="38" height="42" viewBox="0 0 38 42" fill="var(--icon)"><path d="M4 4a4 4 0 0 1 4-4h28v32H9a3 3 0 0 0 0 6h27v4H8a4 4 0 0 1-4-4z"/><rect x="12" y="6" width="18" height="20" fill="#f4f4f4"/><rect x="15" y="9" width="12" height="14"/></svg>
    <span>Document<br>Library</span>
  </div>
  <div class="tile" style="left:24px;top:341px">
    <svg width="42" height="42" viewBox="0 0 42 42" fill="none" stroke="var(--icon)" stroke-width="4.5" stroke-linecap="round"><path d="M18 12l5-5a7 7 0 0 1 10 10l-5 5"/><path d="M24 30l-5 5a7 7 0 0 1-10-10l5-5"/><line x1="16" y1="26" x2="26" y2="16"/></svg>
    <span>Relevant<br>Links</span>
  </div>
  <div class="tile" style="left:204px;top:341px">
    <svg width="44" height="44" viewBox="0 0 44 44"><path d="M16 2h18l8 8v28H16z" fill="#fff" stroke="var(--icon)" stroke-width="2.5"/><path d="M2 10h18v32H2z" fill="#fff" stroke="var(--icon)" stroke-width="2.5"/><rect x="5" y="30" width="3" height="9" fill="var(--icon)"/><rect x="10" y="25" width="3" height="14" fill="var(--icon)"/><rect x="15" y="28" width="3" height="11" fill="var(--icon)"/><g stroke="var(--icon)" stroke-width="2.5"><line x1="6" y1="16" x2="17" y2="16"/><line x1="6" y1="21" x2="17" y2="21"/><line x1="24" y1="14" x2="38" y2="14"/><line x1="24" y1="20" x2="38" y2="20"/><line x1="24" y1="26" x2="38" y2="26"/></g></svg>
    <span>Reports</span>
  </div>
  <div class="tile" style="left:116px;top:434px">
    <svg width="40" height="40" viewBox="0 0 40 40"><rect width="40" height="40" rx="4" fill="var(--icon)"/><rect x="7" y="7" width="11" height="11" fill="#fff"/><circle cx="27.5" cy="12.5" r="5.5" fill="#fff"/><path d="M12.5 22l6 11h-12z" fill="#fff"/><rect x="22" y="22" width="11" height="11" rx="3" fill="#fff"/></svg>
    <span>Forms</span>
  </div>
</section>

</body>
</html>
```